Bref créative
Business card design for dental office
appointment card
Professional
Carla Vostrikov, D.M.D.
4817 Route 92 Building D
Millbrook Falls, VT 05991
carladmd@velmora.net
Appointment Date and Time

```html
<!DOCTYPE html>
<html lang="en">
<head>
<meta charset="utf-8">
<title>Clearwave Dental Stationery</title>
<link href="https://fonts.googleapis.com/css2?family=Lato:wght@400;700&display=swap" rel="stylesheet">
<style>
:root{
  --bg:#2a2a2c;
  --paper:#ffffff;
  --paper-shade:#eef0f2;
  --brand-blue:#1d4e9e;
  --brand-green:#3fa535;
  --ink:#555b63;
  --rule:#c9ccd1;
}
*{margin:0;padding:0;box-sizing:border-box}
html,body{width:1200px;height:761px;overflow:hidden;background:var(--bg);font-family:'Lato',sans-serif}
.canvas{position:relative;width:1200px;height:761px}
.piece{position:absolute;background:var(--paper);box-shadow:0 4px 14px rgba(0,0,0,.45)}
.brand{font-family:'Lato',sans-serif;font-weight:700;color:var(--brand-blue);white-space:nowrap;letter-spacing:.2px}
.small{font-size:6px;color:var(--ink);line-height:1.45;white-space:nowrap}

/* business card */
.business-card{left:53px;top:41px;width:211px;height:127px;border-radius:8px;overflow:hidden}
.business-card .brand{position:absolute;left:0;right:0;top:18px;text-align:center;font-size:15px}
.business-card .holder{position:absolute;left:0;right:0;top:58px;text-align:center;font-size:6.5px;color:var(--ink)}
.business-card .band{position:absolute;left:0;top:72px;width:211px;height:12px}
.business-card .address{position:absolute;left:12px;top:92px}
.business-card .contact{position:absolute;left:120px;top:92px}

/* appointment card */
.appointment-card{left:278px;top:41px;width:214px;height:127px;border-radius:8px;overflow:hidden;padding:12px 14px}
.appointment-card h3{font-size:7.5px;font-weight:700;color:#333;margin-bottom:6px}
.appointment-card .field{display:flex;align-items:flex-end;gap:6px;font-size:6px;color:var(--ink);margin-bottom:5px}
.appointment-card .field span{flex:1;border-bottom:1px solid var(--rule);height:8px}
.appointment-card .row{display:flex;gap:10px}
.appointment-card .row .field{flex:1}
.appointment-card .brand{position:absolute;right:12px;bottom:10px;font-size:8px}

/* envelope flaps */
.envelope-flaps{position:absolute;left:53px;top:180px;width:504px;height:270px}

/* envelope front */
.envelope-front{left:53px;top:492px;width:504px;height:204px;overflow:hidden}
.envelope-front .brand{position:absolute;left:18px;top:26px;font-size:16px}
.envelope-front .address{position:absolute;left:18px;top:70px}
.envelope-front .band{position:absolute;left:0;bottom:14px;width:504px;height:10px}

/* letterhead */
.letterhead{left:643px;top:53px;width:504px;height:667px;overflow:hidden}
.letterhead .brand{position:absolute;left:0;right:0;top:40px;text-align:center;font-size:26px}
.letterhead .band{position:absolute;left:0;top:590px;width:504px;height:14px}
.letterhead .address{position:absolute;left:18px;top:616px}
.letterhead .contact{position:absolute;left:160px;top:614px}
.contact-line{display:flex;align-items:center;gap:4px}
.contact-line svg{width:6px;height:6px;fill:var(--brand-blue)}
</style>
</head>
<body>
<main class="canvas">

  <section class="piece business-card">
    <div class="brand">Clearwave Dental</div>
    <div class="holder">Carla Vostrikov, D.M.D.</div>
    <svg class="band" viewBox="0 0 211 12" preserveAspectRatio="none">
      <polygon points="0,3 90,3 84,12 0,12" fill="var(--brand-green)"/>
      <polygon points="92,3 211,3 211,12 86,12" fill="var(--brand-blue)"/>
    </svg>
    <div class="small address">4817 Route 92 Building D<br>Millbrook Falls, VT 05991</div>
    <div class="small contact">T (555) 014-2261<br>F (555) 014-2262<br>carladmd@velmora.net</div>
  </section>

  <section class="piece appointment-card">
    <h3>Your Next Appointment Is on:</h3>
    <div class="row">
      <div class="field">Date:<span></span></div>
      <div class="field">Time:<span></span></div>
    </div>
    <div class="row">
      <div class="field">Date:<span></span></div>
      <div class="field">Time:<span></span></div>
    </div>
    <div class="row">
      <div class="field">Date:<span></span></div>
      <div class="field">Time:<span></span></div>
    </div>
    <div class="brand">Clearwave Dental</div>
  </section>

  <svg class="envelope-flaps" viewBox="0 0 504 270">
    <rect x="0" y="0" width="504" height="270" fill="var(--paper)"/>
    <polygon points="0,0 504,0 504,6 252,48 0,6" fill="var(--paper-shade)"/>
    <text x="252" y="30" text-anchor="middle" font-family="Lato, sans-serif" font-weight="700" font-size="11" fill="var(--brand-blue)">Clearwave Dental</text>
    <rect x="0" y="84" width="504" height="6" fill="var(--paper-shade)"/>
    <polygon points="0,90 504,90 504,96 252,140 0,96" fill="var(--brand-blue)"/>
    <text x="252" y="120" text-anchor="middle" font-family="Lato, sans-serif" font-weight="700" font-size="11" fill="var(--paper)">Clearwave Dental</text>
    <rect x="0" y="172" width="504" height="6" fill="var(--paper-shade)"/>
    <polygon points="0,178 504,178 504,184 252,232 0,184" fill="var(--brand-green)"/>
    <text x="252" y="208" text-anchor="middle" font-family="Lato, sans-serif" font-weight="700" font-size="11" fill="var(--paper)">Clearwave Dental</text>
  </svg>

  <section class="piece envelope-front">
    <div class="brand">Clearwave Dental</div>
    <div class="small address">4817 Route 92 Building D<br>Millbrook Falls, VT 05991</div>
    <svg class="band" viewBox="0 0 504 10" preserveAspectRatio="none">
      <polygon points="0,0 70,0 64,10 0,10" fill="var(--brand-green)"/>
      <polygon points="72,0 504,0 504,10 66,10" fill="var(--brand-blue)"/>
    </svg>
  </section>

  <section class="piece letterhead">
    <div class="brand">Clearwave Dental</div>
    <svg class="band" viewBox="0 0 504 14" preserveAspectRatio="none">
      <polygon points="0,4 140,4 132,14 0,14" fill="var(--brand-green)"/>
      <polygon points="142,0 504,0 504,14 134,14" fill="var(--brand-blue)"/>
    </svg>
    <div class="small address">4817 Route 92 Building D<br>Millbrook Falls, VT 05991</div>
    <div class="small contact">
      <div class="contact-line"><svg viewBox="0 0 10 10"><path d="M2 0h2l1 3-1.5 1a6 6 0 0 0 2.5 2.5L7 5l3 1v2c0 1-1 2-2 2A8 8 0 0 1 0 2c0-1 1-2 2-2z"/></svg>(555) 014-2261</div>
      <div class="contact-line"><svg viewBox="0 0 10 10"><rect x="1" y="1" width="8" height="8" rx="1"/></svg>(555) 014-2262</div>
      <div class="contact-line"><svg viewBox="0 0 10 10"><path d="M0 2h10v6H0z"/></svg>carladmd@velmora.net</div>
    </div>
  </section>

</main>
</body>
</html>
```